business card for a massage therapy practice named 'Meadow and Willow Massage Studio'

I really need a trendy, yet easy on the eyes business card to complement my logo. Ideally with some gold or rose gold foil work.

My uploaded file of the logo I have in horizontal but I have a vertical version as well. Another color that is used in the website is a blush pink here and there. I'd like to see some trendy tropical leaves in the design.

```html
<!DOCTYPE html>
<html lang="en">
<head>
<meta charset="utf-8">
<title>Meadow and Willow Massage Studio – Business Card</title>
<link rel="stylesheet" href="https://fonts.googleapis.com/css2?family=Nunito:wght@400;600&family=Kaushan+Script&display=swap">
<style>
  :root {
    --backdrop: #ecedeb;
    --mint: #6fd4b6;
    --mint-shade: #5cc2a5;
    --mint-deep: #3f9c82;
    --gold: #c8a04c;
    --paper: #ffffff;
    --ink: #1f1f1f;
    --green-text: #5aa58a;
    --muted: #3a3a3a;
  }
  * { box-sizing: border-box; margin: 0; padding: 0; }
  html, body { width: 1200px; height: 1021px; overflow: hidden; }
  body {
    background: var(--backdrop);
    font-family: "Nunito", Arial, sans-serif;
    position: relative;
  }
  .card {
    position: absolute;
    width: 580px;
    height: 340px;
    border-radius: 6px;
    overflow: hidden;
    box-shadow: 0 10px 24px rgba(0,0,0,0.18);
  }

  /* Front */
  .card-front {
    left: 60px;
    top: 90px;
    background: var(--mint);
  }
  .leaf-decor {
    position: absolute;
    background: radial-gradient(ellipse at center, var(--mint-shade) 0%, rgba(92,194,165,0) 70%);
  }
  .leaf-decor.bottom-left { left: -40px; bottom: -70px; width: 320px; height: 260px; }
  .leaf-decor.top-right { right: -30px; top: -40px; width: 260px; height: 240px; }
  .front-brand {
    position: absolute;
    left: 0; right: 0; top: 118px;
    text-align: center;
    color: var(--gold);
    font-weight: 600;
  }
  .front-brand .brand-mark {
    display: block;
    width: 22px; height: 22px;
    border-radius: 50%;
    background: var(--gold);
    margin: 0 auto 14px;
  }
  .front-brand .brand-name {
    font-size: 30px;
    letter-spacing: 1px;
    line-height: 1.25;
  }

  /* Back */
  .card-back {
    left: 560px;
    top: 590px;
    background: var(--paper);
    border-bottom: 6px solid var(--mint);
  }
  .back-brand {
    position: absolute;
    top: 56px; left: 0; right: 0;
    display: flex;
    align-items: center;
    justify-content: center;
    gap: 14px;
  }
  .back-brand .brand-mark {
    width: 18px; height: 18px;
    border-radius: 50%;
    background: var(--gold);
  }
  .back-brand .brand-name {
    font-weight: 600;
    font-size: 22px;
    color: var(--ink);
    line-height: 1.2;
  }
  .person {
    position: absolute;
    top: 158px; left: 0; right: 0;
    text-align: center;
  }
  .person-name {
    font-family: "Kaushan Script", cursive;
    font-size: 30px;
    color: var(--ink);
  }
  .person-title {
    font-size: 14px;
    color: var(--green-text);
    margin-top: 2px;
  }
  .contact-list {
    position: absolute;
    bottom: 34px; left: 0; right: 0;
    display: flex;
    justify-content: center;
    gap: 30px;
    list-style: none;
    font-size: 14px;
    color: var(--muted);
  }
  .contact-list li { display: flex; align-items: center; gap: 7px; }
  .contact-list svg { width: 15px; height: 15px; fill: none; stroke: var(--green-text); stroke-width: 1.8; }
</style>
</head>
<body>
  <section class="card card-front" aria-label="Business card front">
    <div class="leaf-decor bottom-left" role="img" aria-label="Faint tropical monstera leaf illustration"></div>
    <div class="leaf-decor top-right" role="img" aria-label="Faint tropical palm leaf illustration"></div>
    <div class="front-brand">
      <span class="brand-mark"></span>
      <p class="brand-name">Meadow and Willow<br>Massage Studio</p>
    </div>
  </section>

  <section class="card card-back" aria-label="Business card back">
    <div class="back-brand">
      <span class="brand-mark"></span>
      <p class="brand-name">Meadow and Willow<br>Massage Studio</p>
    </div>
    <div class="person">
      <p class="person-name">Your Name</p>
      <p class="person-title">Job Title</p>
    </div>
    <ul class="contact-list">
      <li>
        <svg viewBox="0 0 24 24"><path d="M5 4h4l2 5-2.5 1.5a11 11 0 0 0 5 5L15 13l5 2v4a2 2 0 0 1-2 2A16 16 0 0 1 3 6a2 2 0 0 1 2-2z"/></svg>
        000 000 0000
      </li>
      <li>
        <svg viewBox="0 0 24 24"><rect x="3" y="5" width="18" height="14" rx="1"/><path d="M3 6l9 7 9-7"/></svg>
        youremail@xyz.com
      </li>
      <li>
        <svg viewBox="0 0 24 24"><circle cx="12" cy="12" r="9"/><path d="M3 12h18M12 3c3 3 3 15 0 18M12 3c-3 3-3 15 0 18"/></svg>
        www.yourwebsite.com
      </li>
    </ul>
  </section>
</body>
</html>
```